Nice concept website for free living

A website for promoting 2 concepts.

---
Live for free in amsterdam -

homeowner? --- or --- searching to rent?

HOMEOWNER PAGE:

instructions on one page --- homeowners can make x amount in a legal way - and click for more information. Form or contact direct by mobile number.

SEARCHING TO RENT PAGE:

First fill out their details quick form --- Available properties --- show available properties.

Target Market(s)

1. People needing a place to live
2. Homeowners that want more revenue from their real estate

Industry/Entity Type

Tourism

Number of Pages Required

3 page

Requirements
Must have
• Simple nice design
• Homepage quick explanation - what is the concept and choice for
• 1. Homeowners
• 2. Renters
Nice to have
• fresh design

```html
<!DOCTYPE html>
<html lang="en">
<head>
<meta charset="UTF-8">
<title>Canalnest – Live for free in Amsterdam</title>
<link href="https://fonts.googleapis.com/css2?family=Jost:wght@400;500;700&display=swap" rel="stylesheet">
<style>
  :root {
    --sky-top: #2f6fae;
    --sky-mid: #1f4c7a;
    --city-dark: #1b2635;
    --city-warm: #7a5430;
    --street-glow: #c9893a;
    --overlay: rgba(10, 22, 38, 0.55);
    --overlay-soft: rgba(10, 22, 38, 0.28);
    --white: #ffffff;
    --green-top: #8dc63f;
    --green-bottom: #5fa32a;
    --accent-yellow: #f2e600;
    --badge-dark: #111111;
  }
  * { margin: 0; padding: 0; box-sizing: border-box; }
  html, body { width: 1200px; height: 640px; overflow: hidden; }
  body { font-family: "Jost", Arial, sans-serif; color: var(--white); }

  .landing {
    position: relative;
    width: 1200px;
    height: 640px;
    overflow: hidden;
  }
  .city-backdrop {
    position: absolute;
    inset: 0;
    background:
      radial-gradient(ellipse at 85% 60%, rgba(201,137,58,0.55), transparent 45%),
      radial-gradient(ellipse at 25% 75%, rgba(201,137,58,0.45), transparent 40%),
      linear-gradient(to bottom, var(--sky-top) 0%, var(--sky-mid) 30%, var(--city-dark) 55%, var(--city-warm) 80%, var(--city-dark) 100%);
  }
  .facets {
    position: absolute;
    inset: 0;
    width: 1200px;
    height: 640px;
  }

  .brand {
    position: absolute;
    top: 136px;
    left: 0;
    width: 100%;
    text-align: center;
    font-weight: 700;
    font-size: 26px;
    letter-spacing: 0.5px;
  }

  .headline {
    position: absolute;
    top: 276px;
    left: 0;
    width: 100%;
    text-align: center;
    font-weight: 700;
    font-size: 48px;
    line-height: 50px;
    letter-spacing: 0.5px;
  }

  .choice {
    position: absolute;
    top: 397px;
    left: 368px;
    display: flex;
    align-items: center;
  }
  .choice-button {
    width: 190px;
    height: 37px;
    border-radius: 19px;
    background: linear-gradient(to bottom, var(--green-top), var(--green-bottom));
    color: var(--white);
    font-family: inherit;
    font-weight: 500;
    font-size: 15px;
    border: none;
    display: flex;
    align-items: center;
    justify-content: center;
  }
  .choice-or {
    width: 37px;
    height: 37px;
    margin: 0 28px 0 24px;
    border-radius: 50%;
    background: var(--badge-dark);
    border: 2px solid var(--white);
    color: var(--accent-yellow);
    font-weight: 500;
    font-size: 13px;
    display: flex;
    align-items: center;
    justify-content: center;
  }

  .footer-copy {
    position: absolute;
    left: 166px;
    top: 590px;
    font-size: 10px;
  }
  .social-links {
    position: absolute;
    left: 910px;
    top: 591px;
    display: flex;
    gap: 16px;
  }
  .social-dot {
    width: 12px;
    height: 12px;
    border-radius: 50%;
    background: var(--white);
  }
</style>
</head>
<body>
  <main class="landing">
    <div class="city-backdrop" role="img" aria-label="Evening panorama of Amsterdam with canal houses, church domes and light trails on the street"></div>

    <svg class="facets" viewBox="0 0 1200 640" aria-hidden="true">
      <polygon points="264,0 936,0 600,336" fill="var(--overlay-soft)"/>
      <polygon points="600,0 780,180 600,360 420,180" fill="var(--overlay)"/>
      <polygon points="96,640 1104,640 600,240" fill="rgba(10,22,38,0.22)"/>
      <polygon points="700,640 1064,640 882,470" fill="rgba(10,22,38,0.18)"/>
    </svg>

    <div class="brand">CANALNEST</div>

    <h1 class="headline">LIVE FOR FREE IN<br>AMSTERDAM</h1>

    <div class="choice">
      <button class="choice-button">Home Owner?</button>
      <span class="choice-or">OR</span>
      <button class="choice-button">Searching to Rent?</button>
    </div>

    <footer>
      <p class="footer-copy">Copyright © 2016. Canalnest. All Right Reserved</p>
      <div class="social-links">
        <span class="social-dot"></span>
        <span class="social-dot"></span>
        <span class="social-dot"></span>
        <span class="social-dot"></span>
        <span class="social-dot"></span>
      </div>
    </footer>
  </main>
</body>
</html>
```